e-commerce store for sport clothing online store "baseball merchandise "web application...

I want to design a UX/UI for my web application website for the online store I will provide you with the following:
1. screen shots of the initial design for the pages>
2. the logo files.
3. The brand guideline file.

the provided files (screen shots) is guideline I want to see CREATIVITY with the UX/UI DESIGN.
PS. PLEASE FOLLOW THE BRANDGUIDE LINE CAREFULLY SPECIALLY THE TYPOGRAPHY & THE COLOR CODES.

PLEASE VISIT THIS WEBSITE morningpath.velrin-qz.com to see more for the screens.

```html
<!DOCTYPE html>
<html lang="en">
<head>
<meta charset="utf-8">
<title>Diamond Nine Store – Screens</title>
<link href="https://fonts.googleapis.com/css2?family=Montserrat:wght@400;500;600;700;800&display=swap" rel="stylesheet">
<style>
:root{
  --page:#ececee;
  --navy:#14284f;
  --navy-deep:#0e1d3b;
  --red:#c8102e;
  --red-dark:#a30c24;
  --white:#ffffff;
  --ink:#14284f;
  --muted:#8a93a6;
  --line:#e1e4ea;
  --panel-bg:#f3f4f7;
}
*{box-sizing:border-box;margin:0;padding:0}
html,body{width:1200px;height:2252px;overflow:hidden}
body{background:var(--page);font-family:'Montserrat',sans-serif;color:var(--ink);position:relative}
.screen{position:absolute;left:36px;width:1128px;height:684px;background:var(--panel-bg);overflow:hidden;box-shadow:0 4px 14px rgba(20,40,79,.18)}
.screen--catalog{top:36px}
.screen--brands{top:780px}
.screen--menu{top:1496px}
.topbar{position:absolute;left:0;top:0;width:100%;height:56px;background:var(--navy)}
.search{position:absolute;right:190px;top:16px;width:170px;height:24px;background:var(--white);border-radius:12px;font-size:11px;color:var(--muted);padding:5px 12px}
.search__btn{position:absolute;right:3px;top:3px;width:18px;height:18px;border-radius:50%;background:var(--red)}
.user{position:absolute;right:60px;top:12px;text-align:right;color:var(--white);font-size:10px;line-height:1.3}
.user strong{display:block;font-size:12px;font-weight:700}
.avatar{position:absolute;right:18px;top:12px;width:32px;height:32px;border-radius:50%;background:#dfe3ec}
.sidebar{position:absolute;left:0;top:0;width:170px;height:100%;background:var(--navy)}
.brand{position:absolute;left:20px;top:14px;width:130px;height:92px;display:flex;flex-direction:column;align-items:center;justify-content:center;gap:8px}
.brand__dot{width:34px;height:34px;border-radius:50%;background:var(--red)}
.brand__name{color:var(--white);font-weight:800;font-size:15px;letter-spacing:.5px}
.side-nav{position:absolute;left:20px;top:180px;list-style:none}
.side-nav li{display:flex;align-items:center;gap:10px;color:var(--white);font-size:11px;font-weight:500;height:32px}
.side-nav i{display:block;width:14px;height:14px;border-radius:50%;background:var(--white)}
.side-nav .alert i{background:var(--red)}
.content{position:absolute;left:196px;top:70px;width:900px;height:566px;background:var(--white);box-shadow:0 2px 8px rgba(20,40,79,.12)}
.ribbon{position:absolute;left:50%;top:18px;transform:translateX(-50%);width:280px;height:38px;background:var(--red);color:var(--white);font-weight:700;font-size:19px;text-align:center;line-height:38px}
.ribbon::before,.ribbon::after{content:"";position:absolute;top:8px;width:26px;height:30px;background:var(--red-dark);z-index:-1}
.ribbon::before{left:-18px}.ribbon::after{right:-18px}
.products{position:absolute;left:20px;top:70px;width:860px;list-style:none}
.product{display:flex;align-items:center;gap:40px;height:140px;border-bottom:1px solid var(--line);padding-left:20px}
.product:last-child{border-bottom:none}
.product__img{width:110px;height:110px;border-radius:4px;flex:none}
.product__img--cap{background:radial-gradient(circle at 50% 55%,#1f2a44 0 40%,#f4f4f6 42%)}
.product__img--tee{background:radial-gradient(circle at 50% 50%,#d9dbe0 0 44%,#f7f7f8 46%)}
.product__img--dark{background:radial-gradient(circle at 50% 50%,#1b1b1f 0 44%,#f7f7f8 46%)}
.product__title{font-size:19px;font-weight:700;line-height:1.35;max-width:620px}
.product__price{font-size:25px;font-weight:800;color:var(--red);margin-top:12px}
.dots{position:absolute;left:50%;bottom:8px;transform:translateX(-50%);display:flex;gap:7px}
.dots span{width:8px;height:8px;border-radius:50%;background:#f2b7c1}
.dots span.on{background:var(--red)}
.footer{position:absolute;left:196px;width:900px;bottom:14px;text-align:center;font-size:9px;color:var(--muted)}
.emblem{position:absolute;left:196px;top:70px;width:900px;height:566px;background:radial-gradient(ellipse at 50% 70%,#e2e6ee 0 38%,rgba(243,244,247,0) 62%)}
.accordion{position:absolute;left:196px;top:78px;width:900px;list-style:none}
.accordion li{height:56px;background:var(--white);border-bottom:1px solid var(--line);display:flex;align-items:center;justify-content:space-between;padding:0 12px 0 20px;font-size:16px;font-weight:700}
.chev{width:36px;height:36px;background:var(--red);border-radius:3px;display:flex;align-items:center;justify-content:center}
.shade{position:absolute;inset:0;background:rgba(20,24,36,.55)}
.drawer{position:absolute;left:0;top:0;width:210px;height:100%;background:var(--red)}
.drawer__close{position:absolute;left:194px;top:0;width:22px;height:22px;background:var(--navy);color:var(--white);font-size:14px;font-weight:700;text-align:center;line-height:22px}
.drawer-nav{position:absolute;left:0;top:16px;width:100%;list-style:none}
.drawer-nav li{display:flex;align-items:center;gap:14px;height:58px;padding-left:26px;color:var(--white);font-size:16px;font-weight:700}
.drawer-nav li.active{background:var(--red-dark)}
.drawer-nav svg{width:18px;height:18px;flex:none}
</style>
</head>
<body>

<!-- Catalog screen -->
<section class="screen screen--catalog">
  <header class="topbar">
    <div class="search">Search<span class="search__btn"></span></div>
    <div class="user">Welcome<strong>Halden N.</strong></div>
    <div class="avatar"></div>
  </header>
  <aside class="sidebar">
    <div class="brand"><span class="brand__dot"></span><span class="brand__name">DIAMOND NINE</span></div>
    <ul class="side-nav">
      <li><i></i>Home</li><li><i></i>Settings ▾</li><li><i></i>Samples ▾</li><li><i></i>Discover</li><li class="alert"><i></i></li>
    </ul>
  </aside>
  <main class="content">
    <div class="ribbon">Salty Marlin</div>
    <ul class="products">
      <li class="product"><div class="product__img product__img--cap" role="img" aria-label="Navy baseball cap"></div><div><p class="product__title">Salty Marlin Logo Hat Step out in style in the salty marlin hat - Salty Marlin logo in front</p><p class="product__price">12.000 KD</p></div></li>
      <li class="product"><div class="product__img product__img--tee" role="img" aria-label="Grey printed t-shirt"></div><div><p class="product__title">Delta Wingpath If you don't have one yourself, you know someone with Labrador.</p><p class="product__price">19.000 KD</p></div></li>
      <li class="product"><div class="product__img product__img--dark" role="img" aria-label="Black printed t-shirt"></div><div><p class="product__title">Reef Drift Crew<br>Turn heads in the Reef Drift Crew Tee.</p><p class="product__price">19.000 KD</p></div></li>
    </ul>
    <div class="dots"><span class="on"></span><span></span><span></span></div>
  </main>
  <p class="footer">© 2024 morningpath.velrin-qz.com All Rights Reserved · Privacy · Terms and Use · Store agreement</p>
</section>

<!-- Brands screen -->
<section class="screen screen--brands">
  <header class="topbar">
    <div class="search">Search<span class="search__btn"></span></div>
    <div class="user">Welcome<strong>Halden N.</strong></div>
    <div class="avatar"></div>
  </header>
  <aside class="sidebar">
    <div class="brand"><span class="brand__dot"></span><span class="brand__name">DIAMOND NINE</span></div>
    <ul class="side-nav">
      <li><i></i>Home</li><li><i></i>Settings ▾</li><li><i></i>Samples ▾</li><li><i></i>Discover</li><li class="alert"><i></i></li>
    </ul>
  </aside>
  <div class="emblem" role="img" aria-label="Faint brand backdrop decoration"></div>
  <ul class="accordion">
    <li>Salty Marlin<span class="chev"><svg width="16" height="10" viewBox="0 0 16 10"><path d="M2 2l6 6 6-6" stroke="#fff" stroke-width="2.5" fill="none"/></svg></span></li>
    <li>Hookline Performance Angling<span class="chev"><svg width="16" height="10" viewBox="0 0 16 10"><path d="M2 2l6 6 6-6" stroke="#fff" stroke-width="2.5" fill="none"/></svg></span></li>
    <li>Quashy Club<span class="chev"><svg width="16" height="10" viewBox="0 0 16 10"><path d="M2 2l6 6 6-6" stroke="#fff" stroke-width="2.5" fill="none"/></svg></span></li>
  </ul>
  <p class="footer">© 2024 morningpath.velrin-qz.com All Rights Reserved · Privacy · Terms and Use · Store agreement</p>
</section>

<!-- Mobile menu screen -->
<section class="screen screen--menu">
  <header class="topbar">
    <div class="search">Search<span class="search__btn"></span></div>
    <div class="user">Welcome<strong>Halden N.</strong></div>
    <div class="avatar"></div>
  </header>
  <aside class="sidebar"></aside>
  <main class="content">
    <div class="ribbon">Salty Marlin</div>
    <ul class="products">
      <li class="product"><div class="product__img product__img--cap" role="img" aria-label="Navy baseball cap"></div><div><p class="product__title">Salty Marlin Logo Hat Step out in style in the salty marlin hat - Salty Marlin logo in front</p><p class="product__price">12.000 KD</p></div></li>
      <li class="product"><div class="product__img product__img--tee" role="img" aria-label="Grey printed t-shirt"></div><div><p class="product__title">Delta Wingpath If you don't have one yourself, you know someone with Labrador.</p><p class="product__price">19.000 KD</p></div></li>
      <li class="product"><div class="product__img product__img--dark" role="img" aria-label="Black printed t-shirt"></div><div><p class="product__title">Reef Drift Crew<br>Turn heads in the Reef Drift Crew Tee.</p><p class="product__price">19.000 KD</p></div></li>
    </ul>
    <div class="dots"><span class="on"></span><span></span><span></span></div>
  </main>
  <div class="shade"></div>
  <nav class="drawer">
    <span class="drawer__close">×</span>
    <ul class="drawer-nav">
      <li class="active"><svg viewBox="0 0 18 18"><path d="M2 9l7-6 7 6v7h-5v-5H7v5H2z" fill="#fff"/></svg>Home</li>
      <li><svg viewBox="0 0 18 18"><path d="M1 3h3l2 9h9l2-7H5" stroke="#fff" stroke-width="2" fill="none"/><circle cx="7" cy="15" r="1.6" fill="#fff"/><circle cx="14" cy="15" r="1.6" fill="#fff"/></svg>My cart</li>
      <li><svg viewBox="0 0 18 18"><circle cx="9" cy="9" r="7" stroke="#fff" stroke-width="2" fill="none"/><path d="M9 5v4l3 2" stroke="#fff" stroke-width="2" fill="none"/></svg>Track Orders</li>
      <li><svg viewBox="0 0 18 18"><path d="M4 2l3 1 1 4-2 1a9 9 0 004 4l1-2 4 1 1 3-2 2C8 16 2 10 2 4z" fill="#fff"/></svg>Contact</li>
    </ul>
  </nav>
</section>

</body>
</html>
```